BRVO Membership Certificate

We are launching an online membership for www.brvo.com

When someone joins they will receive a membership certificate that outlines their name, membership number, membership status, date of membership

```html
<!DOCTYPE html>
<html lang="en">
<head>
<meta charset="utf-8">
<title>BRVO Membership Certificate</title>
<link href="https://fonts.googleapis.com/css2?family=Cinzel:wght@400;700&family=Poppins:wght@400;500&family=Allura&display=swap" rel="stylesheet">
<style>
  :root {
    --navy-deep: #171447;
    --navy: #22296e;
    --gold: #c39c2a;
    --gold-light: #d9bb3c;
    --gold-dark: #a8801e;
    --ink: #161616;
    --paper: #ffffff;
    --rule: #2b3380;
  }
  * { margin: 0; padding: 0; box-sizing: border-box; }
  html, body { width: 1200px; height: 880px; overflow: hidden; background: var(--navy-deep); }
  .certificate { position: relative; width: 1200px; height: 880px; overflow: hidden; font-family: "Poppins", sans-serif; color: var(--ink); }
  .backdrop { position: absolute; inset: 0; width: 100%; height: 100%; }

  .org-box {
    position: absolute; left: 457px; top: 48px; width: 286px; height: 101px;
    background: var(--navy); border: 2px solid var(--navy-deep);
    display: flex; align-items: center; gap: 16px; padding: 0 16px;
  }
  .org-mark { width: 64px; height: 64px; background: var(--paper); flex: none; }
  .org-name {
    font-family: "Poppins", sans-serif; font-weight: 500; font-size: 15.5px; line-height: 1.2;
    color: var(--paper); text-transform: uppercase; letter-spacing: 0.02em;
  }

  .title {
    position: absolute; left: 0; right: 0; top: 172px; text-align: center;
    font-family: "Cinzel", serif; font-weight: 700; font-size: 68px; letter-spacing: 0.06em; color: var(--ink); line-height: 1;
  }
  .subtitle {
    position: absolute; left: 0; right: 0; top: 248px; text-align: center;
    font-family: "Cinzel", serif; font-weight: 400; font-size: 64px; letter-spacing: 0.08em; color: var(--gold); line-height: 1;
  }
  .lead {
    position: absolute; left: 0; right: 0; top: 338px; text-align: center;
    font-family: "Poppins", sans-serif; font-weight: 500; font-size: 24px; letter-spacing: 0.5em; color: var(--ink);
  }
  .recipient {
    position: absolute; left: 232px; width: 708px; top: 392px; height: 62px;
    border-bottom: 1.5px solid var(--rule); text-align: center;
    font-family: "Allura", cursive; font-size: 62px; line-height: 62px; color: var(--navy);
  }

  .statement { position: absolute; left: 120px; width: 910px; top: 522px; font-size: 16px; color: var(--ink); }
  .statement-row { display: flex; align-items: flex-end; height: 42px; gap: 12px; white-space: nowrap; }
  .field {
    flex: 1; border-bottom: 1.5px solid var(--rule); text-align: center;
    font-size: 15px; letter-spacing: 0.22em; color: var(--gold); font-weight: 500; line-height: 22px;
  }
  .field-number { flex: none; width: 675px; }

  .seal { position: absolute; left: 513px; top: 668px; width: 180px; height: 180px; }

  .sign-block { position: absolute; top: 812px; width: 255px; border-top: 1.5px solid var(--gold); text-align: center; }
  .sign-block span { display: block; padding-top: 6px; font-family: "Cinzel", serif; font-weight: 700; font-size: 17px; letter-spacing: 0.04em; color: var(--paper); }
  .sign-signature { left: 80px; }
  .sign-date { left: 862px; }
  .sign-date span { padding-top: 12px; font-size: 15px; }
</style>
</head>
<body>
<main class="certificate">
  <svg class="backdrop" viewBox="0 0 1200 880" preserveAspectRatio="none" aria-hidden="true">
    <defs>
      <linearGradient id="navyFill" x1="0" y1="0" x2="0" y2="1">
        <stop offset="0" stop-color="#171447"/>
        <stop offset="1" stop-color="#232c78"/>
      </linearGradient>
      <linearGradient id="goldFill" x1="0" y1="0" x2="1" y2="1">
        <stop offset="0" stop-color="#a8801e"/>
        <stop offset="0.5" stop-color="#d4b236"/>
        <stop offset="1" stop-color="#b8922a"/>
      </linearGradient>
      <radialGradient id="paperFill" cx="0.5" cy="0.75" r="0.8">
        <stop offset="0" stop-color="#f4f4f4"/>
        <stop offset="0.6" stop-color="#ffffff"/>
      </radialGradient>
      <radialGradient id="sealFill" cx="0.4" cy="0.35" r="0.7">
        <stop offset="0" stop-color="#f7edc4"/>
        <stop offset="0.6" stop-color="#d2ad45"/>
        <stop offset="1" stop-color="#9c7619"/>
      </radialGradient>
    </defs>
    <rect width="1200" height="880" fill="url(#navyFill)"/>
    <polygon points="120,92 480,0 665,0 1200,163 1200,501 1088,656 370,782 0,570 0,272" fill="url(#paperFill)"/>
    <polygon points="665,0 750,0 1200,82 1200,163" fill="url(#goldFill)"/>
    <polygon points="0,150 120,92 0,272" fill="url(#goldFill)"/>
    <line x1="180" y1="0" x2="60" y2="106" stroke="#c39c2a" stroke-width="2"/>
    <polygon points="0,570 370,782 0,631" fill="url(#goldFill)"/>
    <polygon points="370,782 1088,656 1200,634 1200,720 525,790" fill="url(#goldFill)"/>
    <line x1="525" y1="790" x2="560" y2="880" stroke="#c39c2a" stroke-width="2"/>
  </svg>

  <header class="org-box">
    <div class="org-mark"></div>
    <p class="org-name">Northbay Service<br>Excellence<br>Institute</p>
  </header>

  <h1 class="title">BRVO MEMBERSHIP</h1>
  <h2 class="subtitle">CERTIFICATE</h2>
  <p class="lead">THIS CERTIFIES THAT</p>
  <p class="recipient">Dana Whitfield</p>

  <section class="statement">
    <div class="statement-row">Has been granted an honourably life membership in the association in consideration of his</div>
    <div class="statement-row">valuable service as <span class="field">MEMBERSHIP STATUS</span> of</div>
    <div class="statement-row"><span class="field field-number">MEMBERSHIP NUMBER</span> on 15.06.24, Thursday.</div>
  </section>

  <svg class="seal" viewBox="0 0 180 180" role="img" aria-label="Gold membership seal">
    <circle cx="90" cy="90" r="86" fill="url(#sealFill)"/>
    <circle cx="90" cy="90" r="66" fill="#f5f3ee" stroke="#b8922a" stroke-width="3"/>
  </svg>

  <div class="sign-block sign-signature"><span>Signature</span></div>
  <div class="sign-block sign-date"><span>DATE</span></div>
</main>
</body>
</html>
```